I want a business card that is going to show a creative spark but without limiting me to an industry. Something edgy but that wont go out of date. I want it state My business name Verity Lanes, profession - Professional Makeup Artist contact number and email

My service is to provide makeup services from bridal, fashion, photography, film, TV and so on. It is creative and different so i want that to be reflected.

I would like the card double sided.
Updates

 I would LOVE a background on my card something like this image... i can supply an image to be formed like this

Please use the image uploaded

Can we try using the image provided on one side of the card and then writing and details on the other side

Target Market(s)

I am targeting a wide range of people from Creative directors to the individual eg. bride

Industry/Entity Type

Business

Requirements
Must have
• Name: Harriet Cole
contact numbe 0417 583 940
email address:info@veritylanes.example
website: www.veritylanes.example
One of the images attached

professional makeup artist / hair stylist

I want it to show creativity
Nice to have
• logo, Double-sided card
Should not have
• the design should not use tradional style. Or images that are not my own

```html
<!DOCTYPE html>
<html lang="en">
<head>
<meta charset="utf-8">
<title>Verity Lanes – Business Card</title>
<link rel="stylesheet" href="https://fonts.googleapis.com/css2?family=Dawning+of+a+New+Day&display=swap">
<style>
  :root {
    --backdrop: #d8d8d8;
    --card: #232323;
    --card-edge: #1b1b1b;
    --ink: #f4f1ee;
    --ink-soft: #cfc9c4;
    --pink: #c2245e;
    --red: #9e0d14;
    --brown: #7a5a3c;
  }
  * { box-sizing: border-box; margin: 0; padding: 0; }
  html, body {
    width: 1200px;
    height: 900px;
    overflow: hidden;
  }
  body {
    background: var(--backdrop);
    font-family: "Dawning of a New Day", cursive;
    color: var(--ink);
  }
  .sheet {
    position: relative;
    width: 1200px;
    height: 900px;
  }
  .card {
    position: absolute;
    top: 305px;
    width: 540px;
    height: 290px;
    background: var(--card);
    border: 1px solid var(--card-edge);
    box-shadow: 0 4px 10px rgba(0, 0, 0, 0.35);
    overflow: hidden;
  }
  .card--front { left: 40px; }
  .card--back { left: 620px; }

  .brush-area {
    position: absolute;
    display: block;
  }
  .card--front .brush-area {
    left: 290px;
    top: 24px;
    width: 170px;
    height: 196px;
  }
  .card--back .brush-area {
    left: 34px;
    top: 8px;
    width: 240px;
    height: 226px;
  }

  .wordmark {
    position: absolute;
    left: 80px;
    top: 150px;
    font-size: 46px;
    line-height: 42px;
    color: var(--ink);
    font-weight: 400;
  }
  .wordmark__line { display: block; }
  .wordmark__line--second { padding-left: 56px; }

  .tagline {
    position: absolute;
    left: 300px;
    top: 238px;
    font-size: 13px;
    color: var(--ink-soft);
    letter-spacing: 0.3px;
  }

  .contact {
    position: absolute;
    right: 36px;
    top: 126px;
    text-align: right;
  }
  .contact__name {
    font-size: 26px;
    line-height: 34px;
  }
  .contact__phone {
    margin-top: 10px;
    font-size: 25px;
    line-height: 30px;
    letter-spacing: 2px;
  }
  .contact__email,
  .contact__web {
    margin-top: 6px;
    font-size: 19px;
    line-height: 26px;
  }
</style>
</head>
<body>
  <main class="sheet">
    <section class="card card--front" aria-label="Business card front">
      <svg class="brush-area" viewBox="0 0 170 196" role="img" aria-label="Painted makeup brush strokes in pink, red and bronze">
        <defs>
          <linearGradient id="brush-front" x1="0" y1="0" x2="0" y2="1">
            <stop offset="0" stop-color="var(--pink)" stop-opacity="0.75"/>
            <stop offset="0.55" stop-color="var(--red)" stop-opacity="0.75"/>
            <stop offset="1" stop-color="var(--brown)" stop-opacity="0.7"/>
          </linearGradient>
        </defs>
        <rect x="0" y="0" width="170" height="196" rx="14" fill="url(#brush-front)"/>
      </svg>
      <p class="wordmark">
        <span class="wordmark__line">Verity</span>
        <span class="wordmark__line wordmark__line--second">Lanes</span>
      </p>
      <p class="tagline">Professional Makeup Artist</p>
    </section>

    <section class="card card--back" aria-label="Business card back">
      <svg class="brush-area" viewBox="0 0 240 226" role="img" aria-label="Painted makeup brush strokes in pink, red and bronze">
        <defs>
          <linearGradient id="brush-back" x1="0" y1="0" x2="0" y2="1">
            <stop offset="0" stop-color="var(--pink)" stop-opacity="0.75"/>
            <stop offset="0.55" stop-color="var(--red)" stop-opacity="0.75"/>
            <stop offset="1" stop-color="var(--brown)" stop-opacity="0.7"/>
          </linearGradient>
        </defs>
        <rect x="0" y="0" width="240" height="226" rx="14" fill="url(#brush-back)"/>
      </svg>
      <div class="contact">
        <p class="contact__name">Verity Lanes</p>
        <p class="contact__phone">0417 583 940</p>
        <p class="contact__email">info@veritylanes.example</p>
        <p class="contact__web">www.veritylanes.example</p>
      </div>
    </section>
  </main>
</body>
</html>
```